UK landscaping company needs website

We, Brindle Landscapes need a website design for a company based in Surrey, UK. The design should be bold and playful. We have three main areas of work driveways, paving and fencing. It shouldn't be too heavy in text and concentrate on the pictures from previous jobs we've completed. You may use stock images for the design, these can be changed if you are successful. Please don’t just copy the flyer it is just there to provide content.
We have a logo design which we would also like editing slightly.
Here are some of my local competitors
https://www.vexmoorlandscapes.co.uk/

https://www.twinreedgardendesign.com/

https://quarnelllandscapes.co.uk/

Industry/Entity Type

Landscaping

Coding

Coded - Design and coding required

Number of Pages Required

3 page

Font styles to use
Sans Serif

Requirements
Must have
• Pictures of my previous jobs.
Must be mobile friendly
Easy to navigate
Nice to have
• Try to use different colours. It would be good to have some designs that aren’t just black and green.
I’d like some curves in the design.
Should not have
• We install hard landscaping. Think more building/construction and less plants and cutting grass.

```html
<!DOCTYPE html>
<html lang="en">
<head>
<meta charset="utf-8">
<title>Brindle Landscapes</title>
<link href="https://fonts.googleapis.com/css2?family=Lato:ital,wght@0,400;0,700;0,900;1,400&display=swap" rel="stylesheet">
<style>
:root{
  --green:#5db534;
  --green-dark:#4a9a27;
  --mint:#d8f1c8;
  --ink:#2b2b2b;
  --text:#3a3a3a;
  --white:#ffffff;
  --footer:#2d2d2d;
  --dot:#9a9a9a;
}
*{margin:0;padding:0;box-sizing:border-box}
html,body{width:1200px;height:4516px;overflow:hidden;background:var(--white)}
body{position:relative;font-family:"Lato",sans-serif;color:var(--text)}
.abs{position:absolute}
.photo{position:absolute;overflow:hidden}

/* hero */
.hero{left:0;top:0;width:1200px;height:662px;background:linear-gradient(160deg,#8a8478 0%,#a79a85 35%,#8c8a86 60%,#6f6d69 100%)}
.hero-shade{left:0;top:0;width:1200px;height:662px;background:linear-gradient(180deg,rgba(0,0,0,.35),rgba(0,0,0,.1) 40%,rgba(0,0,0,.15))}
.brand{left:74px;top:48px;display:flex;align-items:center;gap:12px;color:var(--white);font-weight:900;font-size:34px;letter-spacing:1px;line-height:1}
.brand-dot{width:22px;height:22px;border-radius:50%;background:var(--green)}
.phone{right:75px;top:30px;display:flex;align-items:center;gap:14px;color:var(--white);font-weight:700;font-size:26px}
.phone-ring{width:44px;height:44px;border:2px solid var(--white);border-radius:50%;display:flex;align-items:center;justify-content:center}
.nav{left:417px;top:98px;display:flex;align-items:center;gap:0;font-size:14px;color:var(--white);text-transform:uppercase}
.nav a{color:inherit;text-decoration:none;padding:11px 22px;border-radius:22px}
.nav a.active{background:var(--green)}
.hero-copy{left:0;top:250px;width:1200px;text-align:center;color:var(--white);text-shadow:0 2px 6px rgba(0,0,0,.35)}
.hero-copy .pre{font-size:48px;font-weight:900;line-height:1}
.hero-copy h1{font-size:70px;font-weight:900;line-height:1.05;margin-top:6px}
.hero-copy .sub{font-size:28px;font-weight:700;margin-top:14px}
.btn{display:inline-block;background:var(--green);color:var(--white);font-weight:700;text-transform:uppercase;text-decoration:none;border-radius:26px;text-align:center}
.hero-btn{left:464px;top:448px;width:272px;height:48px;line-height:48px;font-size:19px}
.dots{display:flex;gap:16px}
.dots span{width:10px;height:10px;border-radius:50%;background:var(--white)}
.dots span.on{background:#111}
.hero-dots{left:557px;top:599px}

/* section titles */
.title{left:0;width:1200px;text-align:center;color:var(--ink);font-weight:900;font-size:38px;text-transform:uppercase}

/* services */
.card{top:820px;width:331px;height:562px;border-radius:166px;background:var(--green);text-align:center;color:var(--white)}
.card .circle{position:absolute;left:18px;top:21px;width:295px;height:295px;border-radius:50%}
.card h3{position:absolute;left:0;top:340px;width:100%;font-size:24px;font-weight:900}
.card p{position:absolute;left:30px;top:384px;width:271px;font-size:16px;line-height:27px;color:#f2fbe9}
.card .more{position:absolute;left:0;top:484px;width:100%;font-size:13px;font-weight:700;color:#1f3d10}

/* about / why */
.band{left:0;width:1200px}
.h2{color:var(--ink);font-weight:900;font-size:40px;line-height:44px;text-transform:uppercase}
.body-copy{font-size:16.5px;line-height:31.5px;color:var(--text)}
.read{height:48px;line-height:48px;font-size:19px;width:199px}

/* gallery */
.tile{border-radius:22px}
.gallery-btn{left:501px;top:3511px;width:198px;height:44px;line-height:44px;font-size:18px}

/* reviews */
.avatar{width:152px;height:152px;border-radius:50%;top:3851px}
.quote{top:4040px;width:310px;text-align:center;font-style:italic;font-size:16px;line-height:25px;color:var(--text)}
.reviewer{top:4155px;width:310px;text-align:center;font-weight:700;font-size:17px;color:var(--green)}
.review-dots{left:552px;top:4263px}
.review-dots span{background:var(--dot);width:12px;height:12px}
.review-dots span.on{background:#333}

/* footer */
.footer{left:0;top:4341px;width:1200px;height:175px;background:var(--footer);color:var(--white);text-align:center}
.footer-nav{display:flex;justify-content:center;gap:45px;margin-top:48px;font-size:14px;font-weight:700}
.copyright{margin-top:18px;font-size:11px;color:#bdbdbd}
.social{display:flex;justify-content:center;gap:22px;margin-top:12px}
.social span{width:18px;height:18px;border-radius:50%;background:#bdbdbd}
</style>
</head>
<body>

<!-- hero -->
<div class="abs hero" role="img" aria-label="Curved block-paved patio with stone walls under construction"></div>
<div class="abs hero-shade"></div>
<div class="abs brand"><span>BRINDLE LANDSCAPES</span><span class="brand-dot"></span></div>
<div class="abs phone">
  <span class="phone-ring">
    <svg width="20" height="20" viewBox="0 0 24 24"><path fill="#fff" d="M6.6 10.8a15.1 15.1 0 0 0 6.6 6.6l2.2-2.2c.3-.3.7-.4 1-.2 1.1.4 2.3.6 3.6.6.6 0 1 .4 1 1V20c0 .6-.4 1-1 1A17 17 0 0 1 3 4c0-.6.4-1 1-1h3.5c.6 0 1 .4 1 1 0 1.3.2 2.5.6 3.6.1.3 0 .7-.2 1z"/></svg>
  </span>
  <span>1-800-555-0142</span>
</div>
<nav class="abs nav">
  <a class="active" href="#">Home</a><a href="#">About Us</a><a href="#">Services</a><a href="#">Gallery</a><a href="#">Latest News</a><a href="#">Contact Us</a>
</nav>
<div class="abs hero-copy">
  <div class="pre">WELCOME TO</div>
  <h1>BRINDLE LANDSCAPES</h1>
  <div class="sub">WE ARE A COMPANY BASED IN SURREY, UK</div>
</div>
<a class="abs btn hero-btn" href="#">Request a Quote</a>
<div class="abs dots hero-dots"><span class="on"></span><span></span><span></span><span></span></div>

<!-- services -->
<h2 class="abs title" style="top:722px">Our Services Areas</h2>
<div class="abs card" style="left:74px">
  <div class="circle" role="img" aria-label="Block-paved driveway in front of a house" style="background:linear-gradient(160deg,#bfbcb5,#8d7f70 55%,#6d655c)"></div>
  <h3>DRIVEWAYS</h3>
  <p>Lorem ipsum dolor sit amet, consectetur adipiscing elit, sed do eiusmod tempor.</p>
  <div class="more">LEARN MORE</div>
</div>
<div class="abs card" style="left:436px">
  <div class="circle" role="img" aria-label="Grey block paving with a drainage channel" style="background:linear-gradient(160deg,#8c8c8a,#6f6f6d 55%,#a8a8a4)"></div>
  <h3>PAVING</h3>
  <p>Lorem ipsum dolor sit amet, consectetur adipiscing elit, sed do eiusmod tempor.</p>
  <div class="more">LEARN MORE</div>
</div>
<div class="abs card" style="left:797px">
  <div class="circle" role="img" aria-label="New timber panel fence with gravel border" style="background:linear-gradient(180deg,#7d9a6a 0%,#7a5a3c 28%,#6a4b30 75%,#9a9a90)"></div>
  <h3>FENCING</h3>
  <p>Lorem ipsum dolor sit amet, consectetur adipiscing elit, sed do eiusmod tempor.</p>
  <div class="more">LEARN MORE</div>
</div>

<!-- about band -->
<svg class="abs band" style="top:1478px" width="1200" height="830" viewBox="0 0 1200 830" aria-hidden="true">
  <path fill="#d8f1c8" d="M0 90 C140 40 260 20 390 70 C520 120 580 140 720 80 C860 20 960 110 1060 70 C1130 40 1170 20 1200 0 L1200 760 C1110 800 1010 820 860 770 C720 720 620 810 460 800 C300 790 160 720 0 750 Z"/>
</svg>
<h2 class="abs h2" style="left:75px;top:1692px">About<br>Brindle Landscapes</h2>
<p class="abs body-copy" style="left:74px;top:1798px;width:520px">Lorem ipsum dolor sit amet, consectetur adipiscing elit, sed do eiusmod tempor incididunt ut labore et dolore magna aliqua. Ut enim ad minim veniam, quis nostrud exercitation ullamco laboris nisi ut aliquip ex ea commodo consequat. Duis aute irure dolor in reprehenderit in voluptate velit esse cillum dolore eu fugiat nulla pariatur. Excepteur sint occaecat cupidatat non proident, sunt in culpa qui officia deserunt mollit anim id est laborum.</p>
<a class="abs btn read" style="left:74px;top:2057px" href="#">Read More</a>
<div class="photo" role="img" aria-label="Workers levelling a freshly poured concrete slab" style="left:615px;top:1678px;width:512px;height:433px;border-radius:40px;background:linear-gradient(180deg,#6e8f4e 0%,#9a8a70 25%,#9ea3a2 45%,#8c9190 100%)"></div>

<!-- why choose -->
<div class="photo" role="img" aria-label="Crew laying stone paving slabs on a site" style="left:74px;top:2381px;width:513px;height:433px;border-radius:40px;background:linear-gradient(150deg,#8a8478,#a8a59e 45%,#7d7a74)"></div>
<h2 class="abs h2" style="left:615px;top:2390px">Why Choose<br>Brindle Landscapes ?</h2>
<p class="abs body-copy" style="left:615px;top:2495px;width:520px">Lorem ipsum dolor sit amet, consectetur adipiscing elit, sed do eiusmod tempor incididunt ut labore et dolore magna aliqua. Ut enim ad minim veniam, quis nostrud exercitation ullamco laboris nisi ut aliquip ex ea commodo consequat. Duis aute irure dolor in reprehenderit in voluptate velit esse cillum dolore eu fugiat nulla pariatur. Excepteur sint occaecat cupidatat non proident, sunt in culpa qui officia deserunt mollit anim id est laborum.</p>
<a class="abs btn read" style="left:615px;top:2754px" href="#">Read More</a>

<!-- gallery band -->
<svg class="abs band" style="top:2880px" width="1200" height="830" viewBox="0 0 1200 830" aria-hidden="true">
  <defs>
    <linearGradient id="galleryWash" x1="0" y1="0" x2="1" y2="1">
      <stop offset="0" stop-color="#c6e6b0"/><stop offset="1" stop-color="#d6efc6"/>
    </linearGradient>
  </defs>
  <path fill="url(#galleryWash)" d="M0 100 C150 60 260 40 400 80 C540 120 620 150 760 90 C900 30 1000 90 1080 50 C1140 20 1180 10 1200 0 L1200 760 C1100 720 1000 690 860 740 C720 790 620 830 460 800 C300 770 160 690 0 720 Z"/>
</svg>
<h2 class="abs title" style="top:3035px">Work Gallery</h2>
<div class="photo tile" role="img" aria-label="Grey porcelain patio steps" style="left:74px;top:3120px;width:422px;height:346px;background:linear-gradient(180deg,#5a4a3e 0%,#9a9893 30%,#c8c7c3 60%,#8e8d89)"></div>
<div class="photo tile" role="img" aria-label="Pale paving beside a lawn" style="left:510px;top:3120px;width:193px;height:167px;background:linear-gradient(135deg,#b9b8b3,#cfcdc8 55%,#6f9a4a)"></div>
<div class="photo tile" role="img" aria-label="Timber pergola over a patio" style="left:722px;top:3120px;width:193px;height:167px;background:linear-gradient(180deg,#7a5c3e,#a08364 55%,#bdb4a6)"></div>
<div class="photo tile" role="img" aria-label="Timber fence along a garden" style="left:930px;top:3120px;width:193px;height:167px;background:linear-gradient(180deg,#8cb0d8 0%,#5d5236 35%,#4f4a30 80%,#6d8e40)"></div>
<div class="photo tile" role="img" aria-label="Swimming pool with sandstone surround" style="left:510px;top:3301px;width:193px;height:165px;background:linear-gradient(180deg,#6f5a48 0%,#3aa6d8 30%,#2f96c8 50%,#c59a72 75%,#b08566)"></div>
<div class="photo tile" role="img" aria-label="Pergola and paved garden corner" style="left:722px;top:3301px;width:193px;height:165px;background:linear-gradient(180deg,#6f5a44,#8b7a66 50%,#c3c0ba)"></div>
<div class="photo tile" role="img" aria-label="Artificial lawn with fenced border" style="left:930px;top:3301px;width:193px;height:165px;background:linear-gradient(180deg,#8cb0d8 0%,#5f6a3a 35%,#4d8a2c 65%,#3f7d24)"></div>
<a class="abs btn gallery-btn" href="#">View All Work</a>

<!-- reviews -->
<h2 class="abs title" style="top:3767px">Customer Reviews</h2>
<div class="photo avatar" role="img" aria-label="Customer portrait" style="left:164px;background:linear-gradient(180deg,#d9d9d9,#6b6b6b 60%,#1f1f1f)"></div>
<div class="photo avatar" role="img" aria-label="Customer portrait" style="left:525px;background:linear-gradient(180deg,#c9c9c9,#8a7b6e 55%,#2a2a2a)"></div>
<div class="photo avatar" role="img" aria-label="Customer couple portrait" style="left:884px;background:linear-gradient(180deg,#b7b2aa,#7c6e62 55%,#55606e)"></div>
<p class="abs quote" style="left:85px">“ Maecenas malesuada luctus ipsum id congue. Nullam eu nulla eget nunc fringilla tempus et id orci. Proin in ante id justo bibendum euismod...”</p>
<p class="abs quote" style="left:446px">“ Maecenas malesuada luctus ipsum id congue. Nullam eu nulla eget nunc fringilla tempus et id orci. Proin in ante id justo bibendum euismod...”</p>
<p class="abs quote" style="left:805px">“ Maecenas malesuada luctus ipsum id congue. Nullam eu nulla eget nunc fringilla tempus et id orci. Proin in ante id justo bibendum euismod...”</p>
<div class="abs reviewer" style="left:85px">NAME HEADING</div>
<div class="abs reviewer" style="left:446px">NAME HEADING</div>
<div class="abs reviewer" style="left:805px">NAME HEADING</div>
<div class="abs dots review-dots"><span class="on"></span><span></span><span></span><span></span></div>

<!-- footer -->
<footer class="abs footer">
  <div class="footer-nav"><span>HOME</span><span>ABOUT US</span><span>SERVICES</span><span>GALLERY</span><span>LATEST NEWS</span><span>CONTACT US</span></div>
  <div class="copyright">Copyright © 2020. Company Name All Right Reserved</div>
  <div class="social"><span></span><span></span><span></span><span></span><span></span><span></span></div>
</footer>

</body>
</html>
```